Tradeora Banner Design for B2B Consulting Firm

Take the already developed logo (attached) and incorporate it into a creative banner design for placement on Tradeora (the social media platform targeting business users). The banner will be used on the firm's company profile page on Tradeora (not yet created).

```html
<!DOCTYPE html>
<html lang="en">
<head>
<meta charset="utf-8">
<title>Corvane Partners – Tradeora Company Banner</title>
<link rel="stylesheet" href="https://fonts.googleapis.com/css2?family=Libre+Baskerville:wght@400;700&display=swap">
<style>
  :root {
    --stage: #ecece8;
    --forest: #3d5e47;
    --forest-deep: #2f4a38;
    --paper: #ffffff;
  }
  * { margin: 0; padding: 0; box-sizing: border-box; }
  html, body {
    width: 1200px;
    height: 929px;
    overflow: hidden;
    background: var(--stage);
  }
  .canvas {
    position: relative;
    width: 1200px;
    height: 929px;
  }
  .banner {
    position: absolute;
    left: 50px;
    top: 329px;
    width: 1100px;
    height: 272px;
    display: block;
    border-radius: 10px;
    overflow: hidden;
  }
  .banner-title,
  .brand-name,
  .banner-url {
    font-family: "Libre Baskerville", Georgia, serif;
    fill: var(--paper);
  }
  .banner-title { font-weight: 700; font-size: 30px; }
  .brand-name { font-weight: 400; font-size: 14px; }
  .banner-url { font-weight: 400; font-size: 12px; letter-spacing: 4.5px; }
  .brand-mark { fill: var(--paper); }
  .rule { stroke: var(--paper); stroke-width: 1; }
  .social-dot { fill: var(--paper); }
</style>
</head>
<body>
<main class="canvas">
  <svg class="banner" viewBox="0 0 1175 290" xmlns="http://www.w3.org/2000/svg">
    <defs>
      <linearGradient id="backdropTone" x1="0" y1="0" x2="1" y2="1">
        <stop offset="0" stop-color="#46684f"/>
        <stop offset="0.55" stop-color="#3d5e47"/>
        <stop offset="1" stop-color="#334f3c"/>
      </linearGradient>
      <linearGradient id="photoTone" x1="0" y1="0" x2="1" y2="1">
        <stop offset="0" stop-color="#f1f1ee"/>
        <stop offset="0.5" stop-color="#c9d0d6"/>
        <stop offset="1" stop-color="#e8e6e1"/>
      </linearGradient>
    </defs>

    <rect class="backdrop-photo" x="0" y="0" width="1175" height="290" fill="url(#backdropTone)"
          role="img" aria-label="Faded photo of a desk workspace with a laptop, tinted dark green"/>

    <polygon class="white-panel" points="782,0 1175,0 1175,290 985,290 962,268 812,268 880,125" fill="var(--paper)"/>
    <polygon class="accent-notch" points="822,0 917,0 868,68" fill="var(--forest)"/>

    <polygon class="feature-photo" points="892,26 1150,26 1066,256 818,256" fill="url(#photoTone)"
             role="img" aria-label="Photo of a hand pointing at charts on a laptop screen beside glasses and papers"/>

    <polygon class="accent-stripe" points="1158,28 1175,4 1175,38 1076,258 1060,250" fill="var(--forest)"/>

    <g class="brand">
      <circle class="brand-mark" cx="30" cy="88" r="6"/>
      <text class="brand-name" x="44" y="93">Corvane Partners</text>
    </g>

    <g class="headline">
      <text class="banner-title" x="520" y="101" text-anchor="middle">Fractional Marketing Services To</text>
      <text class="banner-title" x="520" y="146" text-anchor="middle">B2B Consulting Firm</text>
    </g>

    <g class="web-line">
      <line class="rule" x1="305" y1="186" x2="364" y2="186"/>
      <text class="banner-url" x="520" y="190" text-anchor="middle">www.companywebsite.com</text>
      <line class="rule" x1="675" y1="186" x2="734" y2="186"/>
    </g>

    <g class="social-row">
      <circle class="social-dot" cx="475" cy="225" r="11"/>
      <circle class="social-dot" cx="504" cy="225" r="11"/>
      <circle class="social-dot" cx="534" cy="225" r="11"/>
      <circle class="social-dot" cx="564" cy="225" r="11"/>
    </g>
  </svg>
</main>
</body>
</html>
```